Brantwell Group needs a business card design

We need a new business card design using the logo recently selected in a logo competition on Sketch Harbor. Our business is a consultancy specializing in aviation and energy and the winning business card design will promote an image of precision and professionalism with creativity.

Please use the logo with the name on the front of the card and use a complementary font. Make the back white with either the light grey or dark grey logo.

Target Market(s)

Senior finance and legal leaders at aviation and energy companies

Industry/Entity Type

Management Consulting

Contact Information for Business Card

Peter Oswalt
President
Brantwell Group

www.brantwellgroup.example

(555) 304-9168
po@brantwellgroup.example

Requirements
Must have
• Professional font that goes well with the logo font

```html
<!DOCTYPE html>
<html lang="en">
<head>
<meta charset="utf-8">
<title>Brantwell Group — Business Card</title>
<link rel="stylesheet" href="https://fonts.googleapis.com/css2?family=Questrial&display=swap">
<style>
  :root {
    --backdrop: #2a2a2a;
    --card-dark: #242424;
    --card-white: #ffffff;
    --logo-grey: #8a8a8a;
    --brand-blue: #1f5296;
    --band-blue: #134279;
    --text-light: #f2f2f2;
    --stripe: #ffffff;
  }
  * { margin: 0; padding: 0; box-sizing: border-box; }
  html, body {
    width: 1200px;
    height: 1048px;
    overflow: hidden;
    background: var(--backdrop);
    font-family: "Questrial", "Century Gothic", sans-serif;
  }
  .canvas { position: relative; width: 1200px; height: 1048px; }
  .card {
    position: absolute;
    width: 700px;
    height: 400px;
    border-radius: 4px;
    box-shadow: 0 10px 30px rgba(0,0,0,0.45);
    overflow: hidden;
  }
  .card-back { left: 420px; top: 80px; background: var(--card-white); }
  .card-front { left: 80px; top: 570px; background: var(--card-dark); }

  .wordmark {
    text-transform: uppercase;
    line-height: 1;
    white-space: nowrap;
  }
  .card-back .wordmark {
    position: absolute;
    left: 0; right: 0; top: 180px;
    text-align: center;
    font-size: 40px;
    letter-spacing: 6px;
    color: var(--logo-grey);
  }
  .card-front .wordmark {
    position: absolute;
    left: 40px; top: 44px;
    font-size: 24px;
    letter-spacing: 4px;
    color: var(--brand-blue);
  }

  .contact { position: absolute; left: 40px; top: 150px; }
  .person-name { font-size: 34px; color: var(--text-light); line-height: 1.1; }
  .person-name .surname { color: var(--brand-blue); }
  .person-title { font-size: 19px; color: var(--brand-blue); margin-top: 2px; }
  .contact-lines { list-style: none; margin-top: 20px; }
  .contact-lines li {
    display: flex; align-items: center; gap: 10px;
    font-size: 20px; color: var(--text-light);
    margin-bottom: 9px;
    white-space: nowrap;
  }
  .contact-lines svg { width: 20px; height: 20px; flex: none; }

  .side-band { position: absolute; right: 0; top: 0; width: 170px; height: 400px; }
</style>
</head>
<body>
<main class="canvas">
  <section class="card card-back" aria-label="Card back">
    <div class="wordmark">Brantwell Group</div>
  </section>

  <section class="card card-front" aria-label="Card front">
    <div class="wordmark">Brantwell Group</div>

    <div class="contact">
      <p class="person-name">Peter <span class="surname">Oswalt</span></p>
      <p class="person-title">President</p>
      <ul class="contact-lines">
        <li>
          <svg viewBox="0 0 20 20" aria-hidden="true">
            <path d="M4 3h4l1.5 4-2 1.5a10 10 0 0 0 4 4l1.5-2 4 1.5v4a2 2 0 0 1-2 2A15 15 0 0 1 2 5a2 2 0 0 1 2-2z" fill="var(--brand-blue)"/>
          </svg>
          (555) 304-9168
        </li>
        <li>
          <svg viewBox="0 0 20 20" aria-hidden="true">
            <rect x="1" y="4" width="18" height="12" rx="1.5" fill="var(--brand-blue)"/>
            <path d="M2 5l8 6 8-6" stroke="var(--card-dark)" stroke-width="1.5" fill="none"/>
          </svg>
          po@brantwellgroup.example
        </li>
        <li>
          <svg viewBox="0 0 20 20" aria-hidden="true">
            <circle cx="10" cy="10" r="8" fill="none" stroke="var(--brand-blue)" stroke-width="1.6"/>
            <ellipse cx="10" cy="10" rx="3.5" ry="8" fill="none" stroke="var(--brand-blue)" stroke-width="1.4"/>
            <path d="M2 10h16" stroke="var(--brand-blue)" stroke-width="1.4"/>
          </svg>
          www.brantwellgroup.example
        </li>
      </ul>
    </div>

    <svg class="side-band" viewBox="0 0 170 400" preserveAspectRatio="none" aria-hidden="true">
      <path d="M138 0 C 70 90, 28 230, 20 400 L 170 400 L 170 0 Z" fill="var(--stripe)"/>
      <path d="M150 0 C 84 92, 42 232, 34 400 L 170 400 L 170 0 Z" fill="var(--band-blue)"/>
    </svg>
  </section>
</main>
</body>
</html>
```